Sports Therapy and Personal Training

I need a business card design for a new business based in Toronto called "Vellmore Athletics" I am a sports therapist as well as a strength and conditioning coach, therefore I work mainly with high level athletes and physically active people. I am starting my own therapy/training business. The services I will be offering include fitness consultation, personal training, athlete assessments, and rehabilitation therapy. These services will be delivered in peoples homes and/or a facility in which I rent space.

The final design should communicate "high-end" and "quality"

Target Market(s)

athletes and physically active people

Industry/Entity Type

Fitness

Requirements
Must have
• 1. The business logo - files attached

2. my name and credentials

Derek Vellmore - CAT(C), CK, CSCS,

Certified Athletic Therapist
Strength and Conditioning Specialist

3. website - www.vellmoreathletics.example

4. email address - derek@vellmoreathletics.example

5. phone number

```html
<!DOCTYPE html>
<html lang="en">
<head>
<meta charset="utf-8">
<title>Vellmore Athletics – Business Card</title>
<link rel="stylesheet" href="https://fonts.googleapis.com/css2?family=Archivo:wght@600;700;800;900&display=swap">
<style>
  :root {
    --backdrop: #d2d2d2;
    --card-light: #ffffff;
    --card-light-edge: #ececec;
    --card-dark: #55565a;
    --card-dark-glow: #7a7b80;
    --tab-dark: #6b6c70;
    --tab-light: #ffffff;
    --brand-red: #d0121b;
    --ink: #1e1e20;
    --ink-soft: #4a4a4e;
  }
  * { box-sizing: border-box; margin: 0; padding: 0; }
  html, body { width: 1200px; height: 1056px; overflow: hidden; }
  body {
    background: var(--backdrop);
    font-family: "Archivo", Arial, sans-serif;
    position: relative;
  }
  .card {
    position: absolute;
    top: 27px;
    height: 1010px;
    border-radius: 22px;
    overflow: hidden;
  }
  .card--front {
    left: 58px; width: 528px;
    background: radial-gradient(ellipse at 50% 30%, var(--card-light) 40%, var(--card-light-edge) 100%);
  }
  .card--back {
    left: 609px; width: 566px;
    background: radial-gradient(ellipse at 50% 45%, var(--card-dark-glow) 0%, var(--card-dark) 70%);
  }
  .tab {
    position: absolute; left: 14px; right: 14px; height: 26px;
  }
  .tab--top { top: 0; border-radius: 0 0 12px 12px; }
  .tab--bottom { bottom: 0; border-radius: 12px 12px 0 0; }
  .card--front .tab { background: var(--tab-dark); }
  .card--back .tab { background: var(--tab-light); }

  /* brand lockup */
  .brand {
    position: absolute; left: 0; right: 0;
    display: flex; flex-direction: column; align-items: center;
  }
  .brand-mark {
    width: 96px; height: 96px; border-radius: 50%;
  }
  .brand-name {
    font-weight: 800; text-transform: uppercase; letter-spacing: 1px;
    white-space: nowrap;
  }
  .tagline {
    font-weight: 700; text-transform: uppercase; letter-spacing: 0.5px;
    white-space: nowrap;
  }
  .card--front .brand { top: 200px; }
  .card--front .brand-mark { background: var(--brand-red); margin-bottom: 44px; }
  .card--front .brand-name { font-size: 31px; color: var(--ink-soft); }
  .card--front .tagline { font-size: 12.5px; color: var(--ink-soft); margin-top: 6px; }

  .card--back .brand { top: 330px; }
  .card--back .brand-mark { width: 150px; height: 150px; background: #ffffff; margin-bottom: 170px; }
  .card--back .brand-name { font-size: 37px; color: #ffffff; }
  .card--back .tagline { font-size: 15px; color: #ffffff; margin-top: 6px; }

  /* name block */
  .person { position: absolute; left: 19px; width: 452px; top: 528px; }
  .person-name {
    font-weight: 900; font-size: 44px; color: var(--brand-red);
    text-transform: uppercase; line-height: 1; letter-spacing: 0.5px;
  }
  .credentials {
    text-align: right; font-weight: 700; font-size: 20px; color: var(--ink); margin-top: 2px;
  }
  .roles {
    position: absolute; left: 30px; top: 694px; list-style: none;
  }
  .roles li {
    font-weight: 700; font-size: 18px; color: var(--ink); text-transform: uppercase;
    line-height: 25px; padding-left: 22px; position: relative;
  }
  .roles li::before {
    content: ""; position: absolute; left: 2px; top: 9px;
    width: 7px; height: 7px; border-radius: 50%; background: var(--ink);
  }
  .divider {
    position: absolute; left: 30px; right: 30px; top: 782px; height: 2px;
    background: linear-gradient(90deg, transparent, var(--brand-red) 45%, transparent);
  }
  .contacts { position: absolute; left: 30px; top: 818px; list-style: none; }
  .contacts li {
    display: flex; align-items: center; gap: 14px;
    font-weight: 700; font-size: 20px; color: var(--ink); text-transform: uppercase;
    height: 32px;
  }
  .contacts svg { width: 22px; height: 18px; fill: var(--ink); flex: none; }
</style>
</head>
<body>
  <section class="card card--front">
    <div class="tab tab--top"></div>
    <div class="brand">
      <div class="brand-mark"></div>
      <div class="brand-name">Vellmore Athletics</div>
      <div class="tagline">Sports Medicine • Strength and Conditioning</div>
    </div>
    <div class="person">
      <h1 class="person-name">Derek Vellmore</h1>
      <p class="credentials">CAT(C), CK, CSCS</p>
    </div>
    <ul class="roles">
      <li>Certified Athletic Therapist</li>
      <li>Strength and Conditioning Specialist</li>
    </ul>
    <div class="divider"></div>
    <ul class="contacts">
      <li>
        <svg viewBox="0 0 22 18" aria-hidden="true"><rect x="2" y="2" width="18" height="11" rx="1.5" fill="none" stroke="currentColor" stroke-width="2" style="stroke:#1e1e20"/><rect x="0" y="14" width="22" height="3" rx="1"/></svg>
        00 0000 0000
      </li>
      <li>
        <svg viewBox="0 0 22 18" aria-hidden="true"><rect x="1" y="3" width="20" height="13" rx="1"/><path d="M2 4 L11 11 L20 4" fill="none" stroke="#fff" stroke-width="1.6"/></svg>
        derek@vellmoreathletics.example
      </li>
      <li>
        <svg viewBox="0 0 22 18" aria-hidden="true"><circle cx="11" cy="9" r="8" fill="none" stroke="#1e1e20" stroke-width="2"/><rect x="4" y="8" width="14" height="2"/></svg>
        www.vellmoreathletics.example
      </li>
    </ul>
    <div class="tab tab--bottom"></div>
  </section>

  <section class="card card--back">
    <div class="tab tab--top"></div>
    <div class="brand">
      <div class="brand-mark"></div>
      <div class="brand-name">Vellmore Athletics</div>
      <div class="tagline">Sports Medicine • Strength and Conditioning</div>
    </div>
    <div class="tab tab--bottom"></div>
  </section>
</body>
</html>
```